Velmaran Business Card

Business card for philanthropic organization

Industry/Entity Type

Business

Contact Information for Business Card

Need a very ELEGANT, sober, embossed, formal business card... it should transmit CREDIBILITY. Not looking for a "fun card". would like white, grays or black designs.

Font styles to use
Script

Requirements
Must have
• Embossed look

```html
<!DOCTYPE html>
<html lang="en">
<head>
<meta charset="utf-8">
<title>Velmaran Business Card</title>
<link href="https://fonts.googleapis.com/css2?family=Pinyon+Script&family=Open+Sans:wght@300;400&display=swap" rel="stylesheet">
<style>
  :root {
    --backdrop: #161617;
    --card: #2b2b2c;
    --card-edge: #232324;
    --ink: #e4e4e4;
    --ink-soft: #c9c9c9;
    --rule: #8a8a8a;
    --emboss-light: rgba(255,255,255,0.18);
    --emboss-dark: rgba(0,0,0,0.7);
  }
  * { margin: 0; padding: 0; box-sizing: border-box; }
  html, body {
    width: 1200px; height: 798px; overflow: hidden;
    background: var(--backdrop);
  }
  .card {
    position: absolute; left: 180px; top: 159px;
    width: 840px; height: 480px;
    background: linear-gradient(135deg, #313132 0%, var(--card) 55%, var(--card-edge) 100%);
    border-radius: 4px;
    box-shadow: 0 18px 40px rgba(0,0,0,0.55);
  }
  .emblem {
    position: absolute; left: 90px; top: 170px;
    display: flex; align-items: center; gap: 14px;
    font-family: "Open Sans", sans-serif; font-weight: 400;
    font-size: 30px; letter-spacing: 2px;
    color: var(--ink);
    text-shadow: -1px -1px 0 var(--emboss-dark), 1px 1px 0 var(--emboss-light);
  }
  .emblem-dot {
    width: 26px; height: 26px; border-radius: 50%;
    background: var(--ink-soft);
    box-shadow: inset -2px -2px 3px var(--emboss-dark), 1px 1px 0 var(--emboss-light);
  }
  .divider {
    position: absolute; left: 392px; top: 150px;
    width: 1px; height: 190px;
    background: var(--rule);
    box-shadow: 1px 0 0 var(--emboss-dark);
  }
  .details {
    position: absolute; left: 418px; top: 62px;
    color: var(--ink);
    text-shadow: -1px -1px 0 var(--emboss-dark), 1px 1px 0 var(--emboss-light);
  }
  .name {
    font-family: "Pinyon Script", cursive;
    font-size: 40px; line-height: 46px; font-weight: 400;
  }
  .name + .name { padding-left: 24px; }
  .info {
    font-family: "Open Sans", sans-serif; font-weight: 300;
    font-size: 19px; line-height: 27px; color: var(--ink-soft);
  }
  .title { margin-top: 6px; }
  .address { margin-top: 22px; }
  .contact { margin-top: 18px; }
  .contact-line { display: flex; align-items: center; gap: 12px; }
  .contact-line svg { width: 16px; height: 16px; flex: none; }
</style>
</head>
<body>
  <div class="card">
    <div class="emblem"><span class="emblem-dot"></span>Velmaran</div>
    <div class="divider"></div>
    <div class="details">
      <p class="name">Teodoro Valcárcel</p>
      <p class="name">Nadir Tal Velmaran</p>
      <p class="info title">Potentate 2017</p>
      <div class="info address">
        <p>P.O. Box 0917-05528</p>
        <p>Corvena, Republic of Corvena</p>
      </div>
      <div class="info contact">
        <p class="contact-line">
          <svg viewBox="0 0 16 16" aria-hidden="true"><rect x="4" y="1" width="8" height="14" rx="1.5" fill="none" stroke="currentColor" stroke-width="1.3"/><line x1="7" y1="12.5" x2="9" y2="12.5" stroke="currentColor" stroke-width="1.3"/></svg>
          +(507)-6200-4187
        </p>
        <p class="contact-line">
          <svg viewBox="0 0 16 16" aria-hidden="true"><rect x="1" y="3" width="14" height="10" fill="currentColor"/><polyline points="1,3 8,9 15,3" fill="none" stroke="#2b2b2c" stroke-width="1.3"/></svg>
          t.valcarcel@velmaran.org
        </p>
      </div>
    </div>
  </div>
</body>
</html>
```